Selling my Home Flyer

I need a flyer/brochure for a house listing I am putting together. I will put all of the information together for you to include in the flyer. This will only be a front and back flyer. No extra pages and no staples will be seen. This will be printed by a large office copier, not a professional copier on standard paper. Therefore no crazy dark backgrounds with lots of bleeding colors. Pictures that I want need for sure in there are Aerial with outline, Front from left, and one of the ones showing the large yard. I included a couple sample designs that I don't hate. But feel free to get creative. I will need this on a quick turnaround and I will make comments quickly as well, so submit ASAP.

Target Market(s)

People that will by my house.

Industry/Entity Type

Real Estate Agent

Font styles to use
Serif
Sans Serif

Colors

Designer to choose colors to be used in the design.

Requirements
Must have
• The pictures I mentioned above. And the price and SF and address! I forgot to tell you the address. It is 4817 Birchwell Lane, Palm Beach Gardens, FL 33410.
Should not have
• Anarchy. I don't want it to look too crazy. Should be pretty straight forward.

```html
<!DOCTYPE html>
<html lang="en">
<head>
<meta charset="utf-8">
<title>Listing Flyer – 4817 Birchwell Lane</title>
<link rel="stylesheet" href="https://fonts.googleapis.com/css2?family=Fira+Sans:wght@400;500;600;700&family=Playfair+Display:wght@700;800&display=swap">
<style>
  :root{
    --navy:#333a8a;
    --ink:#1d1d1d;
    --paper:#ffffff;
    --stage:#d9d6d0;
    --rule:#333a8a;
    --serif:"Playfair Display", Georgia, serif;
    --sans:"Fira Sans", Arial, sans-serif;
  }
  *{box-sizing:border-box;margin:0;padding:0}
  html,body{width:1200px;height:800px;overflow:hidden}
  body{background:var(--stage);position:relative;font-family:var(--sans);color:var(--ink)}
  .page{position:absolute;top:48px;width:546px;height:706px;background:var(--paper);overflow:hidden}
  .page--front{left:35px}
  .page--back{left:616px}
  .abs{position:absolute}
  .photo{position:absolute;display:block}
  .hero{left:0;top:0;width:546px;height:297px}
  .tag{position:absolute;background:var(--navy);color:#fff}
  .tag--sale{left:0;top:26px;width:225px;height:88px;font-family:var(--serif);font-weight:700;font-size:48px;line-height:88px;padding-left:21px}
  .tag--price{left:20px;top:273px;width:161px;height:36px;font-weight:700;font-size:24px;line-height:36px;text-align:center}
  .tag--address{left:0;top:26px;width:225px;height:88px;font-weight:700;font-size:19px;line-height:23.5px;padding:11px 0 0 20px}
  .tag--facts{left:20px;top:272px;width:363px;height:60px;font-weight:700;font-size:19px;line-height:23.5px;padding:7px 0 0 30px}
  .tag--facts li{list-style:none;position:relative}
  .tag--facts li::before{content:"•";position:absolute;left:-11px}
  .headline{left:20px;top:318px;width:370px;font-family:var(--serif);font-weight:800;font-size:19px;line-height:23.5px;color:var(--navy);text-transform:uppercase;letter-spacing:-.2px}
  .lead{left:20px;top:374px;width:352px;font-weight:600;font-size:11.6px;line-height:15.2px}
  .details{left:20px;top:443px;width:352px;font-size:10px;line-height:12.9px}
  .agent-ring{left:395px;top:276px;width:132px;height:132px;border-radius:50%;background:var(--paper)}
  .agent-portrait{left:404px;top:285px;width:114px;height:114px;border-radius:50%;background:var(--navy)}
  .agent{left:380px;top:412px;width:162px;text-align:center}
  .agent-name{font-family:var(--serif);font-weight:700;font-size:11.5px;letter-spacing:.3px}
  .agent-role{font-size:10px;margin-top:1px}
  .agent-call{font-family:var(--serif);font-weight:700;font-size:19.5px;margin-top:10px;line-height:22px}
  .agent-phone{font-weight:700;font-size:19.5px;color:var(--navy);line-height:24px}
  .section-head{left:20px;width:506px;height:14px;display:flex;align-items:center;gap:12px;font-family:var(--serif);font-weight:700;font-size:11.5px;text-transform:uppercase;white-space:nowrap}
  .section-head::before,.section-head::after{content:"";flex:1;height:2px;background:var(--rule)}
  .thumb{position:absolute;width:161px;height:105px}
  .caption{position:absolute;width:161px;text-align:center;font-weight:500;font-size:11.5px;text-transform:uppercase}
  .rule{position:absolute;left:20px;width:506px;height:2px;background:var(--rule)}
  .footer{position:absolute;left:20px;top:678px;width:506px;height:22px;display:flex;align-items:center;font-size:10.4px}
  .footer-label{font-weight:600;width:209px}
  .footer-item{display:flex;align-items:center;gap:7px}
  .footer-item--mail{width:206px}
  .icon{width:20px;height:20px;flex:none}
</style>
</head>
<body>

<!-- FRONT -->
<section class="page page--front">
  <div class="photo hero" role="img" aria-label="Front view of the two-storey Mediterranean-style home from the left, with palm trees and landscaped lawn" style="background:linear-gradient(180deg,#8fb4dc 0%,#c9d6de 30%,#e6ddcf 48%,#8a9a6a 70%,#4f7a34 100%)"></div>
  <div class="tag tag--sale">For Sale</div>
  <div class="tag tag--price">$570,000</div>

  <h1 class="abs headline">Pool home on coveted corner lot with oversized yard.</h1>
  <p class="abs lead">This impressive home boasts one of the largest yards in Palm Beach Gardens' most family friendly community, Willowmere. Enjoy the ultimate Florida lifestyle with a beautiful pool &amp; expanded patio areas - perfect for entertaining.</p>
  <p class="abs details">Upgraded features throughout. Custom wood and ship lap details in all bathrooms and loft. New dark wood laminate flooring upstairs. New high-efficiency A/C units with smart thermostats. New pool pump and new heater controlled from your phone! Crown molding throughout. Walk-in closets.&nbsp; Quiet &amp; private cul-de-sac.</p>

  <div class="abs agent-ring"></div>
  <div class="abs agent-portrait" role="img" aria-label="Portrait of the listing agent"></div>
  <div class="abs agent">
    <div class="agent-name">DANA MORROW</div>
    <div class="agent-role">Contact person</div>
    <div class="agent-call">CALL TODAY</div>
    <div class="agent-phone">561-555-0147</div>
  </div>

  <div class="abs section-head" style="top:559px;top:511px">Exterior View</div>
  <div class="thumb" style="left:20px;top:534px;background:linear-gradient(135deg,#6f8f4a,#d8d0bf 55%,#b69a7c)" role="img" aria-label="Courtyard entry with paver walkway"></div>
  <div class="thumb" style="left:192px;top:534px;background:linear-gradient(180deg,#4c6a3a,#8d9a7a 45%,#4fc0cf 70%,#a48f78)" role="img" aria-label="Screened pool with patio"></div>
  <div class="thumb" style="left:364px;top:534px;background:linear-gradient(180deg,#9fc2e4,#e2dccf 45%,#9c8a74 70%,#4f8f35)" role="img" aria-label="Patio with picnic table and large yard"></div>
  <div class="caption" style="left:20px;top:647px">Courtyard Entry</div>
  <div class="caption" style="left:192px;top:647px">Pool</div>
  <div class="caption" style="left:364px;top:647px">Patio and Yard</div>
  <div class="rule" style="top:668px"></div>

  <div class="footer">
    <span class="footer-label">Get in touch for more information:</span>
    <span class="footer-item footer-item--mail">
      <svg class="icon" viewBox="0 0 20 20"><circle cx="10" cy="10" r="10" fill="#333a8a"/><rect x="5" y="6.5" width="10" height="7" rx="1" fill="#fff"/><path d="M5.5 7l4.5 3.5L14.5 7" fill="none" stroke="#333a8a" stroke-width="1.2"/></svg>
      dana@morrowhomes.com
    </span>
    <span class="footer-item">
      <svg class="icon" viewBox="0 0 20 20"><circle cx="10" cy="10" r="10" fill="#333a8a"/><path d="M5 9c0-2 2-3 5-3s5 1 5 3l-2 .6-.6-1.6h-4.8L7 9.6z M6.5 14l1.5-3.5h4l1.5 3.5z" fill="#fff"/></svg>
      561-555-0147
    </span>
  </div>
</section>

<!-- BACK -->
<section class="page page--back">
  <div class="photo hero" role="img" aria-label="Aerial view of the home and lot with the property line outlined" style="background:linear-gradient(90deg,#2f5a2a 0%,#4b6e3a 30%,#a99a86 45%,#3f6a32 65%,#5f8d3e 80%,#9ea3a6 92%,#6f767a 100%)"></div>
  <svg class="abs" style="left:0;top:0" width="546" height="297" viewBox="0 0 546 297" aria-hidden="true">
    <polyline points="132,262 132,6 385,6 409,62 409,272 385,277" fill="none" stroke="#f2e600" stroke-width="2"/>
  </svg>
  <div class="tag tag--address">4817 Birchwell Lane,<br>Palm Beach Gardens,<br>FL 33410</div>
  <ul class="tag tag--facts">
    <li>2,307 Square Feet</li>
    <li>3 bedrooms and 2 ½ bathrooms</li>
  </ul>

  <div class="abs section-head" style="top:342px">Interior View</div>
  <div class="thumb" style="left:20px;top:363px;background:linear-gradient(180deg,#f1f0ec,#d8d4cc 55%,#a9a49b)" role="img" aria-label="Kitchen with island and living area"></div>
  <div class="thumb" style="left:192px;top:363px;background:linear-gradient(180deg,#e9e3d4,#c9bda5 50%,#7a4a34 80%,#c8b79b)" role="img" aria-label="Master bedroom with wooden bed"></div>
  <div class="thumb" style="left:364px;top:363px;background:linear-gradient(135deg,#c7a98a,#e4d7c4 50%,#f3efe8)" role="img" aria-label="Master bathroom with tub and shower"></div>
  <div class="caption" style="left:20px;top:476px">Kitchen</div>
  <div class="caption" style="left:192px;top:476px">Master Bedroom</div>
  <div class="caption" style="left:364px;top:476px">Master Bathroom</div>
  <div class="rule" style="top:499px"></div>

  <div class="abs section-head" style="top:511px">Interior View</div>
  <div class="thumb" style="left:20px;top:534px;background:linear-gradient(135deg,#d9cbb2,#a98a64 45%,#ece7de)" role="img" aria-label="Dining room with chandelier"></div>
  <div class="thumb" style="left:192px;top:534px;background:linear-gradient(180deg,#eadbb8,#e6d3b0 55%,#5a3424)" role="img" aria-label="Loft with dark wood floors"></div>
  <div class="thumb" style="left:364px;top:534px;background:linear-gradient(135deg,#d6d2c9,#9a9488 50%,#4d4f57)" role="img" aria-label="Powder room with vanity"></div>
  <div class="caption" style="left:20px;top:647px">Dining Room</div>
  <div class="caption" style="left:192px;top:647px">Loft</div>
  <div class="caption" style="left:364px;top:647px">Powder Room</div>
  <div class="rule" style="top:668px"></div>

  <div class="footer">
    <span class="footer-label">Get in touch for more information:</span>
    <span class="footer-item footer-item--mail">
      <svg class="icon" viewBox="0 0 20 20"><circle cx="10" cy="10" r="10" fill="#333a8a"/><rect x="5" y="6.5" width="10" height="7" rx="1" fill="#fff"/><path d="M5.5 7l4.5 3.5L14.5 7" fill="none" stroke="#333a8a" stroke-width="1.2"/></svg>
      dana@morrowhomes.com
    </span>
    <span class="footer-item">
      <svg class="icon" viewBox="0 0 20 20"><circle cx="10" cy="10" r="10" fill="#333a8a"/><path d="M5 9c0-2 2-3 5-3s5 1 5 3l-2 .6-.6-1.6h-4.8L7 9.6z M6.5 14l1.5-3.5h4l1.5 3.5z" fill="#fff"/></svg>
      561-555-0147
    </span>
  </div>
</section>

</body>
</html>
```